Harbourline capital partners pty ltd

Hi guys I recently opened a brokerage company. I need a flyer to capture the attention of customers.
I would like something professional and cool at the same time.
My website is harbourcp-example.com.au
I also attached the current flyer. as you can see it lacks of originality and it isn't cool!!!!
Thank you

Target Market(s)

People between the age of 18-50

Industry/Entity Type

Financial Service

Requirements
Must have
• Mast have features and contents that reflects the website
• harbourcp-example.com.au
Nice to have
• Open to anything
Should not have
• Not to sure

```html
<!DOCTYPE html>
<html lang="en">
<head>
<meta charset="utf-8">
<title>Harbourline Capital Partners – Flyer</title>
<link rel="stylesheet" href="https://fonts.googleapis.com/css2?family=Montserrat:wght@300;400;500;600;700&display=swap">
<style>
  :root {
    --blue: #29a8e0;
    --orange: #f7941d;
    --panel-left: #f1f1f1;
    --panel-right: #e4e5e7;
    --ink: #4a4a4a;
    --ink-soft: #5a5a5a;
    --white: #ffffff;
  }
  * { margin: 0; padding: 0; box-sizing: border-box; }
  html, body {
    width: 926px; height: 1200px; overflow: hidden;
    background: #ffffff;
    font-family: "Montserrat", Arial, sans-serif;
  }
  .flyer { position: relative; width: 926px; height: 1200px; overflow: hidden; }
  .shapes { position: absolute; inset: 0; }

  .brand {
    position: absolute; left: 37px; top: 478px;
    display: flex; align-items: center; gap: 14px;
    color: var(--blue); font-weight: 500;
  }
  .brand-dot { width: 40px; height: 40px; border-radius: 50%; background: var(--blue); flex: none; }
  .brand-name { font-size: 27px; line-height: 1.2; letter-spacing: 0.5px; text-transform: uppercase; }

  .headline { position: absolute; left: 37px; top: 612px; }
  .headline-lead { font-size: 35px; font-weight: 600; color: var(--ink); letter-spacing: 0.5px; line-height: 44px; }
  .headline-dream { font-size: 37px; font-weight: 300; color: var(--blue); letter-spacing: 0.5px; line-height: 44px; }

  .intro {
    position: absolute; left: 37px; top: 718px; width: 505px;
    font-size: 15.5px; line-height: 18px; color: var(--ink-soft);
    text-align: justify; font-weight: 400;
  }

  .specialise-title {
    position: absolute; left: 37px; top: 855px;
    font-size: 23px; font-weight: 600; color: var(--blue); letter-spacing: 0.6px;
  }
  .specialise-list {
    position: absolute; left: 37px; top: 900px; width: 520px;
    list-style: none; display: grid;
    grid-template-columns: 165px auto; grid-auto-flow: column; grid-template-rows: repeat(3, 28.5px);
    font-size: 18.5px; color: var(--ink);
  }
  .specialise-list li { display: flex; align-items: center; gap: 9px; }
  .tick { width: 15px; height: 15px; flex: none; }

  .financiers { position: absolute; left: 604px; top: 393px; width: 305px; }
  .side-title { font-size: 23px; font-weight: 600; color: var(--orange); letter-spacing: 0.2px; }
  .side-text {
    margin-top: 8px; font-size: 14.5px; line-height: 18.5px; color: var(--ink-soft);
    text-align: justify; font-weight: 400;
  }
  .side-list { list-style: none; font-size: 14.5px; line-height: 20.5px; color: var(--ink-soft); }
  .side-list li::before { content: "• "; }
  .financiers .side-list { margin-top: 28px; }

  .why { position: absolute; left: 604px; top: 765px; width: 305px; }
  .why .side-list { margin-top: 8px; }

  .contact {
    position: absolute; left: 37px; top: 1093px;
    list-style: none; color: var(--white); font-size: 23px; line-height: 29px; letter-spacing: 0.3px;
  }
  .contact li { display: flex; align-items: center; gap: 9px; }
  .contact-icon { width: 17px; height: 17px; flex: none; }
</style>
</head>
<body>
<main class="flyer">
  <svg class="shapes" width="926" height="1200" viewBox="0 0 926 1200" aria-hidden="false">
    <defs>
      <linearGradient id="photo-tone" x1="0" y1="0" x2="1" y2="1">
        <stop offset="0" stop-color="#cfd8df"/>
        <stop offset="0.35" stop-color="#e9eef1"/>
        <stop offset="0.6" stop-color="#9aa6b2"/>
        <stop offset="1" stop-color="#2c3442"/>
      </linearGradient>
      <clipPath id="panel-clip">
        <path d="M0,512 Q430,318 926,378 L926,1200 L0,1200 Z"/>
      </clipPath>
    </defs>

    <rect class="hero-photo" x="0" y="0" width="926" height="470" fill="url(#photo-tone)"
          role="img" aria-label="Photo of smiling business people in suits shaking hands in a bright office"/>

    <path class="hero-edge" d="M0,452 Q420,290 926,350 L926,1200 L0,1200 Z" fill="var(--white)"/>
    <path class="hero-band" d="M0,460 Q420,302 926,368 L926,1200 L0,1200 Z" fill="var(--orange)"/>

    <g clip-path="url(#panel-clip)">
      <rect x="0" y="0" width="582" height="1200" fill="var(--panel-left)"/>
      <rect x="582" y="0" width="344" height="1200" fill="var(--panel-right)"/>
    </g>

    <path class="footer-band" d="M0,994 L670,1130 C780,1090 870,1030 926,972 L926,1200 L0,1200 Z" fill="var(--blue)"/>
    <path class="footer-stripe" d="M640,1200 C760,1130 860,1068 926,1010 L926,1200 Z" fill="var(--white)"/>
    <path class="footer-wedge" d="M712,1200 C800,1150 870,1090 926,1034 L926,1200 Z" fill="var(--orange)"/>
  </svg>

  <div class="brand">
    <span class="brand-dot"></span>
    <span class="brand-name">Harbourline Capital<br>Partners Pty Ltd</span>
  </div>

  <h1 class="headline">
    <span class="headline-lead">It’s time to finance</span><br>
    <span class="headline-dream">Your Dream</span>
  </h1>

  <p class="intro">Harbourline capital partners is a bespoke brokerage firm established by a team of professionals who bring with them over 50 year’s combined experience in consulting, finance, negotiation, and executive roles within the finance and automotive industry. We strive for excellence, delivering the right solution for our clients in a timely and professional manner.</p>

  <h2 class="specialise-title">WE SPECIALISE IN FINANCING</h2>
  <ul class="specialise-list">
    <li><svg class="tick" viewBox="0 0 16 16"><circle cx="8" cy="8" r="6.8" fill="none" stroke="var(--blue)" stroke-width="1.6"/><path d="M4.8,8.2 L7.2,10.4 L11.2,5.8" fill="none" stroke="var(--blue)" stroke-width="1.6"/></svg>Cars</li>
    <li><svg class="tick" viewBox="0 0 16 16"><circle cx="8" cy="8" r="6.8" fill="none" stroke="var(--blue)" stroke-width="1.6"/><path d="M4.8,8.2 L7.2,10.4 L11.2,5.8" fill="none" stroke="var(--blue)" stroke-width="1.6"/></svg>Boats</li>
    <li><svg class="tick" viewBox="0 0 16 16"><circle cx="8" cy="8" r="6.8" fill="none" stroke="var(--blue)" stroke-width="1.6"/><path d="M4.8,8.2 L7.2,10.4 L11.2,5.8" fill="none" stroke="var(--blue)" stroke-width="1.6"/></svg>Caravans</li>
    <li><svg class="tick" viewBox="0 0 16 16"><circle cx="8" cy="8" r="6.8" fill="none" stroke="var(--blue)" stroke-width="1.6"/><path d="M4.8,8.2 L7.2,10.4 L11.2,5.8" fill="none" stroke="var(--blue)" stroke-width="1.6"/></svg>Jet skis</li>
    <li><svg class="tick" viewBox="0 0 16 16"><circle cx="8" cy="8" r="6.8" fill="none" stroke="var(--blue)" stroke-width="1.6"/><path d="M4.8,8.2 L7.2,10.4 L11.2,5.8" fill="none" stroke="var(--blue)" stroke-width="1.6"/></svg>Trucks</li>
    <li><svg class="tick" viewBox="0 0 16 16"><circle cx="8" cy="8" r="6.8" fill="none" stroke="var(--blue)" stroke-width="1.6"/><path d="M4.8,8.2 L7.2,10.4 L11.2,5.8" fill="none" stroke="var(--blue)" stroke-width="1.6"/></svg>Earth moving Equipmen</li>
  </ul>

  <section class="financiers">
    <h2 class="side-title">Our Financiers include</h2>
    <p class="side-text">We have privileged and specialized access to a wide range of lenders enabling us to tailor solutions which cater to your individual needs. We work with:</p>
    <ul class="side-list">
      <li>Redgum Finance</li>
      <li>Baywater Leasing</li>
      <li>Veltro Motor Finance</li>
      <li>Summit Lane Finance</li>
      <li>Peppercorn Asset finance</li>
      <li>Norvale Auto Finance</li>
      <li>Grove and General Finance</li>
      <li>Kestrel Marine Finance</li>
      <li>Bluewren Bank Finance</li>
    </ul>
  </section>

  <section class="why">
    <h2 class="side-title">Why use us</h2>
    <ul class="side-list">
      <li>Low rates</li>
      <li>Access Australia’s most<br>trusted lenders</li>
      <li>Quick &amp; easy, same day approvals</li>
      <li>Professional advice</li>
      <li>New, Used, private or dealer sale<br>- the choice is yours</li>
      <li>100% Finance available</li>
    </ul>
  </section>

  <ul class="contact">
    <li><svg class="contact-icon" viewBox="0 0 16 16"><path d="M3.5,1.5 L6,1.5 L7,5 L5.3,6.2 C6.2,8.2 7.8,9.8 9.8,10.7 L11,9 L14.5,10 L14.5,12.5 C14.5,13.6 13.6,14.5 12.5,14.5 C6.9,14.5 1.5,9.1 1.5,3.5 C1.5,2.4 2.4,1.5 3.5,1.5 Z" fill="var(--orange)"/></svg>+61 400 555 018</li>
    <li><svg class="contact-icon" viewBox="0 0 16 16"><rect x="1.5" y="3.5" width="13" height="9" fill="none" stroke="var(--orange)" stroke-width="1.5"/><path d="M1.5,3.5 L8,9 L14.5,3.5" fill="none" stroke="var(--orange)" stroke-width="1.5"/></svg>admin@harbourcp-example.com.au</li>
    <li><svg class="contact-icon" viewBox="0 0 16 16"><circle cx="8" cy="8" r="6.5" fill="none" stroke="var(--orange)" stroke-width="1.4"/><ellipse cx="8" cy="8" rx="3" ry="6.5" fill="none" stroke="var(--orange)" stroke-width="1.2"/><path d="M1.5,8 L14.5,8 M2.8,4.5 L13.2,4.5 M2.8,11.5 L13.2,11.5" stroke="var(--orange)" stroke-width="1.1"/></svg>www.harbourcp-example.com.au</li>
  </ul>
</main>
</body>
</html>
```